Start-Up für Training, Coaching & Consulting sucht modernes Webdesign!
Zielgruppe
Wer ist VELTA Training, Coaching & Consulting?
Wir führen Führungskräftetrainings durch, machen Privatkunden für Bewerbungen fit und unterstützen Unternehmen mit Verkaufstrainings. Wir entwickeln Persönlichkeiten im Coaching. Wir beraten Unternehmen und helfen ihnen dabei, ihre Geschäftsabläufe und Prozesse zu optimieren. Dabei steht unsere hohe Qualität im Mittelpunkt - gemeinsam mit unseren kreativen Trainingsmethoden. Unser Background (Diplom-Kaufleute und geprüfte Trainer) bietet dafür die passende Ausgangslage.
Was bedeutet VELTA?
Velta ist Maori und bdeutet Kreis/Spirale. Er symbolisiert einen wachsenden Silberfarn und steht für persönliche Entwicklung und Entfaltung. Der Velta ist einerseits unser Namensgeber und unser Logo, andererseits steht der Velta aber auch für unsere Werte: Denn wir wollen unseren Kunden dabei helfen zu wachsen und sich weiterzuentwickeln - und dies auf eine hochqualitative und seriöse Art und Weise ohne den Eindruck von Esoterik oder Erlebnispädagogik zu vermitteln.
Aufgabenstellung
Modernes Design, das unsere Philosophie widerspiegelt: Wir möchten unseren Kunden auf seriöse und hochqualitative Weise weiterentwickeln. Wir stehen für nachhaltigen Lernerfolg, kreative Trainingsmethoden, Abwechslung, Spaß am Lernen, Qualität, Kompetenz, Fachwissen und Dynamik.
Layout:
1) Header: GNWR geprüfter Trainer, Menüpunkte (siehe Architektur)
2) Banner
3) 3 Teaser (Training, Coaching, Consulting) + Header + 2-3 Zeilen Text (+Icons)
>>> Sichtbarer Bereich auf Homepage: Menü, Banner, Teaser
4) "Warum Sie uns wählen sollten": 5 bullet points ohne weiteren Text
5) "Aus unserem Blog": Frame für 3 Blogartikel + Bild + Datum + Header + 2-3 Zeilen Text
6) Alle drei GNWR Logos
7) Footer: Click Us (quick links), Contact Us (Adresse), Follow Us (Pagelinq, ZUMO, Workvine)
8) Copyright + Impressum
>>> Das Design soll klar sein, aber nicht zu kantig. Vielmehr sollen abgerundete Ecken und dynamische Elemente genutzt werden.
Architektur:
3 Ebenen:
1) Homepage
2) VELTA, Training, Coaching, Consulting, für Trainer, Kundenstimmen/Referenzen, Kontakt
3) noch zu bestimmende Produktdetailseiten
Texte werden noch erstellt, Layout kann ggf. mit Platzhaltertext gefüllt werden.
Bildmaterial: Logo und vorhandenes Imagebild werden zur Verfügung gestellt. Bilder können ggf. gekauft werden. Vorschläge erwünscht.
Corporate colors:
grün: #a2c61b + monochromatic colors
http://www.tintrix-beispiel.de/a2c61b
grau: #474747 + monochromatic colors
http://www.tintrix-beispiel.de/474747

```html
<!DOCTYPE html>
<html lang="de">
<head>
<meta charset="utf-8">
<title>VELTA – Training · Coaching · Consulting</title>
<link href="https://fonts.googleapis.com/css2?family=Exo+2:wght@300;400;500&display=swap" rel="stylesheet">
<style>
:root{
  --green:#a2c61b;
  --green-dark:#5f8a1e;
  --grey:#474747;
  --dark:#2a2a2a;
  --text:#222;
  --white:#fff;
  --cert:#1e5fa8;
}
*{margin:0;padding:0;box-sizing:border-box}
html,body{width:1200px;height:2409px;overflow:hidden}
body{position:relative;background:var(--white);font-family:"Exo 2",sans-serif;color:var(--text)}
.abs{position:absolute}

/* hero */
.hero{left:0;top:0;width:1200px;height:495px;
  background:
    radial-gradient(ellipse 160px 190px at 560px 270px,rgba(200,225,120,.55),transparent 70%),
    radial-gradient(ellipse 260px 130px at 1000px 120px,rgba(170,210,90,.55),transparent 70%),
    radial-gradient(ellipse 220px 120px at 140px 420px,rgba(150,195,70,.45),transparent 70%),
    radial-gradient(ellipse 300px 160px at 900px 420px,rgba(120,175,50,.5),transparent 70%),
    radial-gradient(ellipse at 50% 40%,#6f9f34 0%,#3e6e22 55%,#1f4414 100%)}
.hero-wave{left:0;top:380px}
.site-header{left:35px;top:7px;width:1130px;height:97px;background:var(--white);border-radius:10px;box-shadow:0 2px 8px rgba(0,0,0,.08)}
.brand{left:42px;top:22px}
.brand-name{font-size:38px;font-weight:500;color:var(--grey);letter-spacing:1px;line-height:1}
.brand-tag{font-size:8px;color:var(--grey);margin-top:6px}
.main-nav{left:266px;top:43px;display:flex;font-size:17px;color:var(--grey)}
.main-nav a{color:inherit;text-decoration:none;display:flex;align-items:center;gap:8px}
.main-nav .active{color:var(--green)}
.cert-badge{left:982px;top:41px;width:98px;height:28px;background:var(--cert);border-radius:3px 14px 3px 3px}
.hero-title{left:121px;top:214px;font-size:38px;line-height:44px;color:var(--white);font-weight:400;text-shadow:0 1px 3px rgba(0,0,0,.25)}
.hero-sub{left:123px;top:320px;font-size:20px;line-height:24px;color:var(--white);text-shadow:0 1px 3px rgba(0,0,0,.25)}
.dots{left:123px;top:388px;display:flex;gap:9px}
.dots span{width:12px;height:12px;border-radius:50%;background:var(--white)}
.dots span:first-child{background:var(--green)}
.arrow{top:263px}

/* teasers */
.teaser{top:590px;width:360px;text-align:center}
.teaser .photo{width:256px;height:256px;border-radius:50%;margin:0 auto;border:4px solid #e6e6e6;position:relative}
.teaser.featured .photo{border:5px solid var(--green)}
.teaser .badge{position:absolute;left:50%;bottom:-14px;margin-left:-34px;width:68px;height:68px;border-radius:50%;background:var(--grey);display:flex;align-items:center;justify-content:center}
.teaser.featured .badge{background:var(--green)}
.teaser h3{margin-top:48px;font-size:22px;font-weight:400;color:var(--text)}
.teaser.featured h3{color:var(--green)}
.teaser p{margin-top:10px;font-size:13.5px;line-height:17px}
.btn{display:inline-block;margin-top:24px;width:114px;height:44px;line-height:42px;border:1.5px solid var(--grey);border-radius:22px;font-size:17px;color:var(--grey)}
.featured .btn{background:var(--green);border-color:var(--green);color:var(--white)}

/* choose */
.section-title{left:0;width:1200px;top:1267px;text-align:center;font-size:31px;color:var(--green);font-weight:400}
.section-lead{left:0;width:1200px;top:1310px;text-align:center;font-size:16px;line-height:19px;color:var(--grey)}
.reasons{left:91px;top:1489px;list-style:none}
.reason{position:relative;width:381px;height:35px;margin-bottom:26px;border:1.5px solid var(--green);border-radius:10px;padding-left:78px;line-height:32px;font-size:16px;color:var(--green)}
.reason.on{background:var(--green);color:var(--white)}
.reason .ico{position:absolute;left:-2px;top:-3px;width:38px;height:38px;border-radius:50%;background:var(--white);border:1.5px solid var(--green);display:flex;align-items:center;justify-content:center}
.reason.on .ico{background:var(--green);border:3px solid var(--white);box-shadow:0 0 0 1.5px var(--green)}
.rule{left:600px;top:1459px;width:1px;height:335px;background:#bbb}
.blog-title{left:635px;top:1452px;font-size:21px;color:var(--grey);font-weight:400}
.post{left:635px;width:435px;display:flex;gap:23px}
.post .thumb{width:88px;height:68px;border-radius:12px 0 12px 0;flex:none;
  background:
    radial-gradient(ellipse 22px 18px at 30% 75%,rgba(235,180,80,.8),transparent 70%),
    radial-gradient(ellipse 20px 16px at 72% 78%,rgba(230,150,90,.7),transparent 70%),
    linear-gradient(90deg,#dfe7ee 0 18%,#9fb0bf 18% 22%,#e9eef2 22% 48%,#9fb0bf 48% 52%,#e4eaf0 52% 100%)}
.post .date{font-size:13px;color:var(--green);line-height:15px}
.post h4{font-size:14px;font-weight:400;line-height:17px}
.post p{font-size:11px;line-height:14px;margin-top:2px}
.sep{left:635px;width:435px;border-top:1px dashed #999}

/* partners */
.partner{background:var(--cert)}

/* footer */
.footer-wave{left:0;top:2055px}
.footer{left:0;top:2120px;width:1200px;height:289px;background:var(--dark);color:var(--white)}
.footer .col{position:absolute;font-size:14px;line-height:17px;font-weight:300}
.footer h5{font-size:19px;font-weight:400;margin-bottom:15px}
.footer .hl{color:var(--green)}
.socials{display:flex;gap:11px}
.socials span{width:26px;height:26px;border-radius:50%;background:var(--green)}
.copyright{left:0;width:1200px;top:2371px;text-align:center;font-size:14px;color:var(--white);font-weight:300}
</style>
</head>
<body>

<div class="abs hero" role="img" aria-label="Nahaufnahme eines sich entrollenden grünen Farnwedels"></div>
<svg class="abs hero-wave" width="1200" height="120" viewBox="0 0 1200 120">
  <path d="M0 80 Q600 140 1200 55 L1200 120 L0 120Z" fill="var(--green)"/>
  <path d="M0 95 Q600 130 1200 68 L1200 120 L0 120Z" fill="#fff"/>
</svg>

<header class="abs site-header">
  <div class="abs brand">
    <div class="brand-name">VELTA</div>
    <div class="brand-tag">Training · Coaching · Consulting</div>
  </div>
  <nav class="abs main-nav">
    <a class="active" style="width:134px">Startseite</a>
    <a style="width:143px">Leistungen <svg width="11" height="8"><path d="M1 1l4.5 5L10 1" stroke="#a2c61b" stroke-width="2" fill="none"/></svg></a>
    <a style="width:140px">Für Trainer <svg width="11" height="8"><path d="M1 1l4.5 5L10 1" stroke="#a2c61b" stroke-width="2" fill="none"/></svg></a>
    <a style="width:146px">Referenzen</a>
    <a>Kontakt</a>
  </nav>
  <div class="abs cert-badge" role="img" aria-label="Zertifikat geprüfter Trainer"></div>
</header>

<h1 class="abs hero-title">Nachhaltiger Lernerfolg durch<br>kreative Trainingsmethoden</h1>
<p class="abs hero-sub">Wir helfen Ihnen dabei zu wachsen und<br>sich weiterzuentwickeln</p>
<div class="abs dots"><span></span><span></span><span></span></div>
<svg class="abs arrow" style="left:35px" width="36" height="44"><path d="M30 4L8 22l22 18" stroke="#ddd" stroke-width="8" fill="none"/></svg>
<svg class="abs arrow" style="left:1128px" width="36" height="44"><path d="M6 4l22 18L6 40" stroke="#ddd" stroke-width="8" fill="none"/></svg>

<section>
  <div class="abs teaser" style="left:27px">
    <div class="photo" role="img" aria-label="Schwarzweißfoto eines Trainers mit Tablet vor einer Gruppe" style="background:radial-gradient(ellipse 50px 110px at 52% 55%,#3a3a3a,transparent 75%),radial-gradient(ellipse 60px 90px at 12% 70%,#555,transparent 75%),linear-gradient(180deg,#e4e4e4 0%,#b5b5b5 50%,#6a6a6a 100%)">
      <div class="badge"><svg width="34" height="34" viewBox="0 0 34 34" fill="#fff"><circle cx="16" cy="10" r="7"/><path d="M3 32c0-9 6-13 13-13s13 4 13 13z"/></svg></div>
    </div>
    <h3>TRAINING</h3>
    <p>Lorem ipsum dolor sit amet, consetetur sadipscing elitr,<br>sed diam nonumy eirmod tempor invidunt ut labore et<br>dolore magna aliquyam erat, sed diam voluptua.</p>
    <span class="btn">Mehr</span>
  </div>
  <div class="abs teaser featured" style="left:420px">
    <div class="photo" role="img" aria-label="Hand bedient ein Tablet auf einem Schreibtisch" style="background:radial-gradient(ellipse 90px 40px at 60% 45%,#f7f9fb,transparent 75%),radial-gradient(ellipse 70px 50px at 30% 55%,#e3c2a8,transparent 75%),linear-gradient(180deg,#dfe8ef 0%,#b7c6d2 55%,#b49a7e 85%,#8d7359 100%)">
      <div class="badge"><svg width="34" height="34" viewBox="0 0 34 34" fill="none" stroke="#fff" stroke-width="2"><rect x="16" y="4" width="14" height="11"/><circle cx="9" cy="8" r="3"/><path d="M9 12v10M5 32h24M9 22l-3 10M9 22l3 10"/></svg></div>
    </div>
    <h3>COACHING</h3>
    <p>Lorem ipsum dolor sit amet, consetetur sadipscing elitr,<br>sed diam nonumy eirmod tempor invidunt ut labore et<br>dolore magna aliquyam erat, sed diam voluptua.</p>
    <span class="btn">Mehr</span>
  </div>
  <div class="abs teaser" style="left:805px">
    <div class="photo" role="img" aria-label="Schwarzweißfoto einer Gruppe im Beratungsgespräch" style="background:radial-gradient(ellipse 45px 100px at 48% 45%,#bdbdbd,transparent 75%),radial-gradient(ellipse 50px 60px at 15% 70%,#6b6b6b,transparent 75%),radial-gradient(ellipse 50px 70px at 85% 70%,#555,transparent 75%),linear-gradient(90deg,#f2f2f2 0 30%,#9a9a9a 30% 32%,#eee 32% 100%)">
      <div class="badge"><svg width="34" height="34" viewBox="0 0 34 34" fill="#fff"><circle cx="12" cy="12" r="6"/><path d="M1 30c0-8 5-11 11-11s11 3 11 11z"/><circle cx="25" cy="9" r="4"/></svg></div>
    </div>
    <h3>CONSULTING</h3>
    <p>Lorem ipsum dolor sit amet, consetetur sadipscing elitr,<br>sed diam nonumy eirmod tempor invidunt ut labore et<br>dolore magna aliquyam erat, sed diam voluptua.</p>
    <span class="btn">Mehr</span>
  </div>
</section>

<svg class="abs" style="left:0;top:1140px" width="1200" height="40"><defs><linearGradient id="fade" x1="0" x2="1"><stop offset="0" stop-color="#a2c61b" stop-opacity=".1"/><stop offset=".5" stop-color="#a2c61b"/><stop offset="1" stop-color="#a2c61b" stop-opacity=".6"/></linearGradient></defs><path d="M0 12 Q500 42 1200 18" stroke="url(#fade)" stroke-width="4" fill="none"/></svg>

<h2 class="abs section-title">Wählen Sie Uns</h2>
<p class="abs section-lead">Lorem ipsum dolor sit amet, consetetur sadipscing elitr, sed diam nonumy<br>eirmod tempor invidunt ut labore et dolore magna aliquyam erat, sed diam voluptua. At vero eos et accusam et justo duo dolores et ea rebum.</p>

<ul class="abs reasons">
  <li class="reason on"><span class="ico"><svg width="18" height="18" fill="none" stroke="#fff" stroke-width="1.5"><rect x="8" y="2" width="8" height="6"/><circle cx="5" cy="4" r="2"/><path d="M5 7v5M2 16h14"/></svg></span>Lorem ipsum dolor sit amet</li>
  <li class="reason"><span class="ico"><svg width="18" height="18" fill="none" stroke="#a2c61b" stroke-width="1.5"><rect x="8" y="2" width="8" height="6"/><circle cx="5" cy="4" r="2"/><path d="M5 7v5M2 16h14"/></svg></span>Lorem ipsum dolor sit amet</li>
  <li class="reason"><span class="ico"><svg width="18" height="18" fill="none" stroke="#a2c61b" stroke-width="1.5"><rect x="8" y="2" width="8" height="6"/><circle cx="5" cy="4" r="2"/><path d="M5 7v5M2 16h14"/></svg></span>Lorem ipsum dolor sit amet</li>
  <li class="reason"><span class="ico"><svg width="18" height="18" fill="none" stroke="#a2c61b" stroke-width="1.5"><rect x="8" y="2" width="8" height="6"/><circle cx="5" cy="4" r="2"/><path d="M5 7v5M2 16h14"/></svg></span>Lorem ipsum dolor sit amet</li>
  <li class="reason"><span class="ico"><svg width="18" height="18" fill="none" stroke="#a2c61b" stroke-width="1.5"><rect x="8" y="2" width="8" height="6"/><circle cx="5" cy="4" r="2"/><path d="M5 7v5M2 16h14"/></svg></span>Lorem ipsum dolor sit amet</li>
</ul>

<div class="abs rule"></div>
<h3 class="abs blog-title">Unser Blog</h3>

<article class="abs post" style="top:1506px">
  <div class="thumb" role="img" aria-label="Gruppe im hellen Seminarraum"></div>
  <div><div class="date">21.12.2015 - 12:48 Uhr</div><h4>Kreative Trainingsmethoden</h4><p>Lorem ipsum dolor sit amet, consectetur adipisicing elit, sed do eiusmod tempor incididunt ut labore et dolore magna aliqua.</p></div>
</article>
<div class="abs sep" style="top:1593px"></div>
<article class="abs post" style="top:1609px">
  <div class="thumb" role="img" aria-label="Gruppe im hellen Seminarraum"></div>
  <div><div class="date">21.12.2015 - 12:48 Uhr</div><h4>Kreative Trainingsmethoden</h4><p>Lorem ipsum dolor sit amet, consectetur adipisicing elit, sed do eiusmod tempor incididunt ut labore et dolore magna aliqua.</p></div>
</article>
<div class="abs sep" style="top:1694px"></div>
<article class="abs post" style="top:1708px">
  <div class="thumb" role="img" aria-label="Gruppe im hellen Seminarraum"></div>
  <div><div class="date">21.12.2015 - 12:48 Uhr</div><h4>Kreative Trainingsmethoden</h4><p>Lorem ipsum dolor sit amet, consectetur adipisicing elit, sed do eiusmod tempor incididunt ut labore et dolore magna aliqua.</p></div>
</article>

<div class="abs partner" role="img" aria-label="Partnerzertifikat geprüfter Trainer" style="left:326px;top:2000px;width:134px;height:36px;border-radius:3px 16px 3px 3px"></div>
<div class="abs partner" role="img" aria-label="Mitgliedschaftszeichen des Verbands" style="left:559px;top:1989px;width:42px;height:54px;border-radius:2px"></div>
<div class="abs partner" role="img" aria-label="Zeichen des Berufsverbands" style="left:748px;top:1988px;width:44px;height:56px;border-radius:2px"></div>

<svg class="abs footer-wave" width="1200" height="70" viewBox="0 0 1200 70">
  <path d="M0 30 Q600 75 1200 0 L1200 70 L0 70Z" fill="var(--green)"/>
  <path d="M0 42 Q600 75 1200 14 L1200 70 L0 70Z" fill="var(--dark)"/>
</svg>
<footer class="abs footer">
  <div class="col" style="left:46px;top:50px">
    <div style="font-size:32px;font-weight:500;line-height:1">VELTA</div>
    <div style="font-size:7px;margin-top:5px">Training · Coaching · Consulting</div>
    <p style="margin-top:22px;width:310px">Lorem ipsum dolor sit amet, consectetur adipisicing elit, sed do eiusmod <span class="hl">tempor incididunt ut</span> labore et dolore magna aliqua.</p>
  </div>
  <div class="col" style="left:426px;top:52px"><h5>Quicklinks</h5>Startseite<br>Referenzen<br>Kontakt<br>Impressum</div>
  <div class="col" style="left:718px;top:52px"><h5>Kontakt</h5>VELTA GmbH<br>Lindenhof 4b<br>23999 Grünwalde<br><br>Tel: &nbsp;&nbsp;&nbsp;0450 12 34 567<br>E-Mail: info@velta-beispiel.de</div>
  <div class="col" style="left:993px;top:52px"><h5>Folgen</h5>
    <div class="socials"><span aria-label="Pagelinq"></span><span aria-label="Workvine"></span><span aria-label="ZUMO"></span></div>
  </div>
</footer>
<p class="abs copyright">© Copyright 2016 - All Rights Reserved</p>

</body>
</html>
```